Ember & Rise Product Formulation & Benefits

Ember and Rise's formulation represents a complex formulation of essential all natural ingredients that reduce stress & anxiety, improve mood, with an elevated mood and euphoric sense of well-being, deliver three stage energy boosters, grass fed bovine collagen and vitamins B6 and B12.
based upon the complexity and the range of physical and mental health benefits we are seeking an animated infographic that will educate consumers on the ingredients and their benefits.

Target Market(s)

Coffee, Hemp and Funcational Beverage Consumers

Industry/Entity Type

Functional Food & Beverage

Requirements
Must have
• cross reference of ingredients to their benefits (see website)
Nice to have
• a concept of a puzzle that comes together, each piece with info on it, that when complete illustrates an image of a healthy lifestyle, coffees beverages, with company logo.

```html
<!DOCTYPE html>
<html lang="en">
<head>
<meta charset="utf-8">
<title>Ember &amp; Rise – Our All-Natural Ingredients</title>
<link href="https://fonts.googleapis.com/css2?family=Arvo:wght@700&family=Bebas+Neue&family=Poppins:wght@400;600;800&display=swap" rel="stylesheet">
<style>
  :root {
    --page: #ffffff;
    --panel: #111111;
    --coral: #e8694a;
    --mint: #3ee3a9;
    --teal-dark: #2a9c98;
    --teal-light: #93d5c6;
    --badge: #5fe6b4;
    --bar: #2b2b2b;
    --ink: #ffffff;
    --body: #e6e6e6;
  }
  * { margin: 0; padding: 0; box-sizing: border-box; }
  html, body { width: 1200px; height: 675px; overflow: hidden; background: var(--page); }
  .canvas { position: relative; width: 1200px; height: 675px; }
  .board {
    position: absolute; left: 55px; top: 31px; width: 1089px; height: 612px;
    background: var(--panel); overflow: hidden;
    box-shadow: 0 8px 22px rgba(0,0,0,.28);
    font-family: "Poppins", sans-serif; color: var(--body);
  }
  .hero-photo {
    position: absolute; left: 470px; top: 0; width: 619px; height: 612px;
    background:
      radial-gradient(ellipse 180px 110px at 230px 400px, #d9d4cc 0%, #9a948c 40%, transparent 75%),
      radial-gradient(ellipse 220px 80px at 300px 560px, #3a2418 0%, transparent 80%),
      radial-gradient(ellipse 170px 320px at 420px 290px, #5c5c5e 0%, #363638 55%, transparent 85%),
      linear-gradient(90deg, #111 0%, #262626 35%, #2c2c2c 100%);
  }
  .title-vertical {
    position: absolute; left: 21px; top: 557px; transform-origin: left top; transform: rotate(-90deg);
    font-family: "Arvo", serif; font-weight: 700; font-size: 26px; line-height: 1; letter-spacing: 1px;
    color: var(--coral); white-space: nowrap;
  }
  .puzzle { position: absolute; left: 62px; top: 0; width: 140px; height: 612px; }
  .section { position: absolute; left: 214px; }
  .section-head {
    display: flex; align-items: center; gap: 6px;
    font-family: "Bebas Neue", sans-serif; font-size: 16px; line-height: 1; color: var(--mint);
    letter-spacing: .2px; white-space: nowrap;
  }
  .section-head::after { content: ""; height: 1px; background: var(--mint); flex: 0 0 var(--rule, 30px); }
  .copy { position: absolute; font-size: 6.6px; line-height: 1.13; color: var(--body); }
  .copy b { font-weight: 600; color: var(--ink); display: block; }
  .benefits { position: absolute; left: 864px; top: 140px; width: 225px; list-style: none; }
  .benefit { position: relative; height: 55.6px; }
  .benefit-bar {
    position: absolute; left: 26px; right: 0; top: 6px; height: 44px; background: var(--bar);
  }
  .benefit-badge {
    position: absolute; left: 0; top: 2px; width: 52px; height: 52px; border-radius: 50%;
    background: var(--badge); border: 2px solid #2a2a2a;
    display: flex; align-items: center; justify-content: center;
  }
  .benefit-label {
    position: absolute; left: 62px; top: 15px; font-weight: 800; font-size: 12.5px; line-height: .92;
    color: var(--ink); text-transform: uppercase; letter-spacing: -.2px; white-space: nowrap;
  }
  .brand-name {
    position: absolute; right: 40px; top: 560px;
    font-family: "Poppins", sans-serif; font-weight: 800; font-size: 15px; line-height: 1;
    color: var(--ink); white-space: nowrap;
  }
</style>
</head>
<body>
<div class="canvas">
  <section class="board">
    <div class="hero-photo" role="img" aria-label="Athlete sprinting past a steaming cup of coffee on a saucer with roasted coffee beans"></div>

    <h1 class="title-vertical">OUR ALL - NATURAL INGREDIENTS</h1>

    <svg class="puzzle" viewBox="0 0 140 612" aria-hidden="true">
      <g fill="var(--teal-dark)">
        <rect x="24" y="22" width="92" height="78"/>
        <circle cx="70" cy="14" r="10"/>
        <rect x="24" y="244" width="92" height="97"/>
        <rect x="24" y="441" width="92" height="97"/>
      </g>
      <g fill="var(--teal-light)">
        <rect x="24" y="118" width="92" height="97"/>
        <circle cx="12" cy="166" r="14"/><circle cx="128" cy="166" r="14"/>
        <rect x="24" y="343" width="92" height="97"/>
        <circle cx="12" cy="391" r="14"/><circle cx="128" cy="391" r="14"/>
        <rect x="24" y="540" width="92" height="57"/>
        <circle cx="12" cy="575" r="14"/><circle cx="128" cy="575" r="14"/>
      </g>
      <g fill="var(--panel)">
        <circle cx="24" cy="68" r="12"/><circle cx="116" cy="68" r="12"/>
        <circle cx="24" cy="290" r="12"/><circle cx="116" cy="290" r="12"/>
        <circle cx="24" cy="488" r="12"/><circle cx="116" cy="488" r="12"/>
      </g>
      <g fill="var(--teal-dark)">
        <circle cx="70" cy="110" r="12"/><circle cx="70" cy="339" r="12"/><circle cx="70" cy="537" r="12"/>
      </g>
      <g fill="var(--teal-light)">
        <circle cx="70" cy="225" r="12"/><circle cx="70" cy="440" r="12"/>
      </g>
      <g fill="#10201f">
        <path d="M70 48 l4 14 l10 -6 l-6 12 h-16 l-6 -12 l10 6z"/><rect x="69" y="68" width="2" height="10"/>
        <circle cx="70" cy="172" r="12"/><rect x="60" y="152" width="20" height="4" rx="2" transform="rotate(-30 70 154)"/>
        <path d="M56 270 h8 l-4 10z M66 270 h8 l-4 10z M76 270 h8 l-4 10z M56 284 h8 l-4 10z M66 284 h8 l-4 10z M76 284 h8 l-4 10z"/>
        <ellipse cx="62" cy="388" rx="9" ry="12"/><ellipse cx="78" cy="394" rx="9" ry="12"/>
        <circle cx="70" cy="494" r="12"/><rect x="68" y="476" width="4" height="8"/>
        <circle cx="76" cy="556" r="4"/><path d="M72 562 l-8 12 l-8 4 M70 568 l8 8 M66 566 l-10 -2" stroke="#10201f" stroke-width="3" fill="none" stroke-linecap="round"/>
      </g>
    </svg>

    <div class="section" style="top:47px">
      <h2 class="section-head" style="--rule:28px">Hemp Derived Delta-9 THC &amp; CBD</h2>
      <p class="copy" style="top:15px;width:225px">Micro-dosing D-9THC, offers health benefits with its psychoactive properties. It reduces anxiety, improves mood, promotes better sleep, enhances focus and creativity, and benefits cognitive tasks. Effects vary among individuals, so consult a healthcare professional before starting any new regimen.</p>
    </div>

    <div class="section" style="top:131px">
      <h2 class="section-head" style="--rule:330px">Adaptogens</h2>
      <p class="copy" style="top:16px;left:0;width:135px"><b>Ashwagandha:</b>An adaptogenic herb used in Ayurvedic medicine, offers numerous benefits. It can reduce stress, enhance mood, and improve cognitive function. By regulating cortisol levels and increasing BDNF levels, it helps combat stress, fatigue, and promotes memory and cognitive function</p>
      <p class="copy" style="top:16px;left:152px;width:120px"><b>Rhodiola: Rhodiola:</b>Is an adaptogenic herb that has been shown to reduce stress, improve mood, and enhance cognitive function. Rhodiola has been shown to increase levels of BDNF, which can help improve memory and cognitive function.</p>
      <p class="copy" style="top:16px;left:284px;width:135px"><b>Bacopa Monnier:</b>Bacopa Monnieri is an adaptogenic herb that has been used in Ayurvedic medicine to enhance cognitive function, improve memory, and reduce anxiety. Bacopa has been shown to increase acetylcholine levels, a neurotransmitter that is essential for learning and memory.</p>
    </div>

    <div class="section" style="top:244px">
      <h2 class="section-head" style="--rule:30px">Grass-Fed Collagen Protein</h2>
      <p class="copy" style="top:15px;width:210px">Adding 15 grams of Grass-fed collagen to your daily routine can strengthen your hair, skin, and digestive function, potentially improving joint health and replenishing lost collagen due to the natural aging process.</p>
    </div>

    <div class="section" style="top:325px">
      <h2 class="section-head" style="--rule:370px">Nootropics</h2>
      <p class="copy" style="top:16px;left:0;width:160px"><b>Instant, Arabica Coffee:</b>Our blend of organic, freeze-dried Arabica coffee is rich in antioxidants, chlorogenic acid, and caffeine, which can help boost energy levels, improve focus, and promote a sense of well-being. Coffee has been shown to increase BDNF levels, a protein that plays a key role in brain health and cognitive function.</p>
      <p class="copy" style="top:16px;left:180px;width:150px"><b>Organic Coffeeberry Extract:</b>Coffee berry extract is a potent antioxidant that has been shown to improve cognitive function, reduce inflammation, and promote healthy aging. Coffee berry extract contains chlorogenic acid, which can help increase BDNF levels and improve memory and cognitive function.</p>
      <p class="copy" style="top:16px;left:348px;width:120px"><b>L-Theanine:</b>L-Theanine, found in tea and mushrooms, promotes relaxation without drowsiness. This popular supplement may enhance mental focus, sleep quality, and cognitive performance. It's also known to reduce stress and anxiety.</p>
    </div>

    <div class="section" style="top:431px">
      <h2 class="section-head" style="--rule:75px">Vitamins B6 &amp; B12:</h2>
      <p class="copy" style="top:16px;width:200px">Vitamins B6 and B12 are crucial for overall health. B6 supports brain development and function, and aids in producing serotonin, norepinephrine, and melatonin. B12 is essential for nerve function, red blood cell formation, and DNA synthesis. It also improves mental clarity, mood, and heart health.</p>
    </div>

    <div class="section" style="top:516px">
      <h2 class="section-head" style="--rule:300px">Energy Boosters</h2>
      <p class="copy" style="top:15px;left:0;width:130px"><b>Ancient Peat &amp; Apple Extract:</b>The combination of "ancient peat" and apple skin extracts. Using innovative biotechnology stimulates your body's endogenous production of adenosine triphosphate (ATP), the veritable energetic currency of cells, providing sustained non-stimulatory energy.</p>
      <p class="copy" style="top:15px;left:145px;width:140px"><b>Medium Chain Triglycerides (MCT):</b>MCT Oil, a blend of coconut and acacia fiber, is a notable supplement for energy, metabolism, and cognitive function. It supports gut health, boosts endurance, and fuels the brain by increasing ketone levels. Always consult a healthcare professional before starting any new supplement regimen.</p>
      <p class="copy" style="top:15px;left:304px;width:105px"><b>Natural Caffeine Anhydrous:</b>Natural Caffeine Anhydrous is a dehydrated, concentrated form of caffeine extracted from natural sources. It's used as a stimulant to enhance alertness, energy, and mental focus.</p>
    </div>

    <ul class="benefits">
      <li class="benefit"><span class="benefit-bar"></span><span class="benefit-badge"><svg width="34" height="34" viewBox="0 0 34 34" fill="none" stroke="#111" stroke-width="2"><circle cx="17" cy="17" r="12"/><circle cx="17" cy="17" r="6"/><path d="M17 1v10M17 23v10M1 17h10M23 17h10"/></svg></span><span class="benefit-label">Experience<br>Increased Focus</span></li>
      <li class="benefit"><span class="benefit-bar"></span><span class="benefit-badge"><svg width="32" height="32" viewBox="0 0 32 32" fill="none" stroke="#111" stroke-width="2"><circle cx="16" cy="16" r="13"/><path d="M9 18h14l-2 4h-10z"/></svg></span><span class="benefit-label">Elevated<br>Mood</span></li>
      <li class="benefit"><span class="benefit-bar"></span><span class="benefit-badge"><svg width="32" height="32" viewBox="0 0 32 32" fill="none" stroke="#111" stroke-width="2"><circle cx="16" cy="15" r="11"/><circle cx="16" cy="15" r="5"/><path d="M13 15l2 2 4-4"/></svg></span><span class="benefit-label">Improved<br>Focus</span></li>
      <li class="benefit"><span class="benefit-bar"></span><span class="benefit-badge"><svg width="32" height="32" viewBox="0 0 32 32" fill="none" stroke="#111" stroke-width="2"><path d="M16 14c-4-5-9-1-5 3l5 4 5-4c4-4-1-8-5-3z"/><path d="M6 6l3 4M26 6l-3 4M10 30v-6M22 30v-6"/></svg></span><span class="benefit-label">Euphoric Sense<br>of Well-Being</span></li>
      <li class="benefit"><span class="benefit-bar"></span><span class="benefit-badge"><svg width="32" height="32" viewBox="0 0 32 32" fill="none" stroke="#111" stroke-width="2"><circle cx="16" cy="8" r="4"/><path d="M6 10l6 8h8l6-8M12 18l-2 10M20 18l2 10"/></svg></span><span class="benefit-label">Reducing Stress<br>and Anxiety</span></li>
      <li class="benefit"><span class="benefit-bar"></span><span class="benefit-badge"><svg width="32" height="32" viewBox="0 0 32 32" fill="none" stroke="#111" stroke-width="2"><rect x="7" y="12" width="18" height="14" rx="2"/><path d="M20 4h5l-5 5h5"/></svg></span><span class="benefit-label">Deep Restorative<br>Sleep</span></li>
      <li class="benefit"><span class="benefit-bar"></span><span class="benefit-badge"><svg width="32" height="32" viewBox="0 0 32 32" fill="none" stroke="#111" stroke-width="2" stroke-linecap="round"><circle cx="20" cy="6" r="3"/><path d="M17 11l-5 8-6 3M16 15l6 5-2 8M13 12l-6 1M18 12l5 3"/></svg></span><span class="benefit-label">Increased and<br>Sustained Energy</span></li>
    </ul>

    <p class="brand-name">Ember &amp; Rise</p>
  </section>
</div>
</body>
</html>
```